Vorminta - Plastic to Diesel Energy Needs A Website

Make website explaining the concept and the team behind the company
Updates

I will be providing A logo and Information about the company upon signed NDA.

Coding

Coded - Design and coding required

Number of Pages Required

5+ page

```html
<!DOCTYPE html>
<html lang="en">
<head>
<meta charset="utf-8">
<title>Vorminta – Plastic to Diesel Energy</title>
<link rel="stylesheet" href="https://fonts.googleapis.com/css2?family=Roboto:wght@400;500;700&display=swap">
<style>
:root{
  --green:#7cc242;
  --green-dark:#6bb035;
  --blue:#1a6fb8;
  --blue-deep:#1d5f9c;
  --ink:#1b1b1b;
  --muted:#666;
  --footer:#121212;
  --white:#fff;
}
*{box-sizing:border-box;margin:0;padding:0}
html,body{width:1200px;height:3898px;overflow:hidden}
body{font-family:"Roboto",Arial,sans-serif;color:var(--ink);background:var(--white);position:relative}
.abs{position:absolute}
/* header */
.site-header{position:absolute;left:0;top:0;width:1200px;height:115px;background:#fff}
.brand{position:absolute;left:110px;top:30px;width:260px}
.brand-name{font-size:40px;font-weight:700;color:var(--blue);letter-spacing:1px;line-height:1}
.brand-tag{font-size:15px;color:var(--green);margin-top:4px;letter-spacing:.5px}
.topbar{position:absolute;left:411px;top:0;width:789px;height:54px;background:var(--green);clip-path:polygon(30px 0,100% 0,100% 100%,0 100%,0 0);display:flex;align-items:center;gap:50px;padding-left:64px;color:#fff;font-size:16px}
.topbar span{display:flex;align-items:center;gap:8px}
.topbar svg{width:15px;height:15px;fill:#fff}
.nav{position:absolute;left:452px;top:76px;display:flex;gap:29px;font-size:16px;color:#444}
.nav a{color:inherit;text-decoration:none;position:relative;padding-bottom:12px}
.nav a.active{color:var(--blue);font-weight:500}
.nav a.active::after{content:"";position:absolute;left:0;right:0;bottom:-27px;height:4px;background:var(--blue)}
/* hero */
.hero{position:absolute;left:0;top:115px;width:1200px;height:580px;background:linear-gradient(100deg,#164c63 0%,#1f6f86 55%,#1c6a80 100%)}
.hero h1{position:absolute;left:110px;top:113px;width:560px;font-size:52px;line-height:67px;color:#fff;font-weight:700}
.hero h1 em{font-style:normal;color:var(--green)}
.hero p{position:absolute;left:110px;top:330px;width:400px;font-size:15px;line-height:25px;color:#fff}
.btn{display:inline-block;font-size:15px;padding:11px 16px;border-radius:3px;text-decoration:none}
.btn-green{background:var(--green);color:#fff}
.btn-white{background:#fff;color:var(--ink)}
.hero .actions{position:absolute;left:110px;top:440px;display:flex;gap:12px}
.hero-art{position:absolute;left:580px;top:20px;width:560px;height:540px;border-radius:50%;background:radial-gradient(circle,#3d8a6a 0%,#2d7b88 50%,rgba(31,111,134,0) 72%)}
/* section titles */
.sec-title{position:absolute;left:0;width:1200px;text-align:center;font-size:44px;font-weight:400}
.sec-title b{font-weight:700;color:var(--blue)}
/* industries */
.sub{position:absolute;left:0;top:846px;width:1200px;text-align:center;font-size:16px;font-weight:500;color:#444}
.card{position:absolute;top:908px;width:312px;height:333px;background:#fff;border-radius:8px;box-shadow:0 3px 14px rgba(0,0,0,.12)}
.card .ph{position:absolute;left:9px;top:9px;width:294px;height:262px;border-radius:6px}
.card h3{position:absolute;left:0;width:100%;text-align:center;font-size:19px;font-weight:500;top:288px}
.card.feature .ph{height:168px}
.card.feature .badge{position:absolute;left:134px;top:154px;width:44px;height:44px;border-radius:50%;background:#fff;display:flex;align-items:center;justify-content:center}
.card.feature h3{top:206px;color:var(--green);font-weight:700}
.card.feature p{position:absolute;left:30px;right:30px;top:238px;text-align:center;font-size:11px;line-height:21px;color:#555}
.arrow{position:absolute;width:30px;height:30px;border-radius:50%;display:flex;align-items:center;justify-content:center}
.arrow svg{width:14px;height:14px;stroke:#fff;stroke-width:3;fill:none}
.arrow.prev{background:var(--blue)}
.arrow.next{background:#cfcfcf}
/* how */
.how{position:absolute;left:0;top:1327px;width:1200px;height:531px;background:var(--green)}
.how .sec-title{top:56px;color:#fff}
.how .sec-title b{color:#fff}
.step{position:absolute;top:165px;width:226px;text-align:center;color:#fff}
.step .ic{width:82px;height:82px;border-radius:50%;margin:0 auto;display:flex;align-items:center;justify-content:center}
.step .ic svg{width:40px;height:40px}
.step .ic.blue{background:var(--blue)}
.step .ic.white{background:#fff}
.step .ribbon{margin-top:24px;height:52px;font-size:20px;font-weight:700;display:flex;align-items:center;justify-content:center;clip-path:polygon(0 0,92% 0,100% 50%,92% 100%,0 100%,6% 50%)}
.step .ribbon.w{background:#fff;color:var(--blue);clip-path:polygon(0 0,92% 0,100% 50%,92% 100%,0 100%)}
.step .ribbon.b{background:var(--blue);color:#fff}
.step .ribbon.w2{background:#fff;color:var(--blue)}
.step h4{margin-top:20px;font-size:20px;font-weight:700}
.step p{margin-top:8px;font-size:12px;line-height:25px;padding:0 4px}
/* about */
.about-img{position:absolute;left:110px;top:1961px;width:447px;height:359px;border-radius:0 0 80px 0;background:linear-gradient(135deg,#3a5a7a,#8a9aa8 55%,#6b6f5a)}
.about h2{position:absolute;left:643px;top:1940px;font-size:44px;font-weight:400}
.about h2 b{color:var(--blue);font-weight:700}
.about p{position:absolute;left:643px;width:445px;font-size:13.5px;line-height:30px;color:#777;text-align:justify}
/* why */
.why{position:absolute;left:0;top:2409px;width:1200px;height:557px;background:var(--blue-deep)}
.why .sec-title{top:44px;color:#fff}
.why .sec-title b{color:#fff}
.why-item{position:absolute;color:#fff}
.why-item h4{font-size:19px;font-weight:500;margin-bottom:6px}
.why-item p{font-size:13px;line-height:26px}
.why-item.l{text-align:right}
.why-ic{position:absolute;width:60px;height:60px;border-radius:50%;background:#fff;display:flex;align-items:center;justify-content:center}
.why-ic svg{width:30px;height:30px}
.emblem{position:absolute;left:500px;top:160px;width:200px;height:300px;border-radius:50%;background:radial-gradient(circle,rgba(255,255,255,.85),rgba(124,194,66,.6) 50%,rgba(29,95,156,0) 72%)}
/* team */
.member{position:absolute;top:3144px;width:236px}
.member .ph{height:253px;border-radius:4px}
.member span{display:block;margin-top:22px;padding-left:9px;font-size:22px;color:#222}
/* footer */
.footer{position:absolute;left:0;top:3544px;width:1200px;height:354px;background:var(--footer);color:#fff}
.footer .brand{left:118px;top:62px}
.sub-form{position:absolute;left:112px;top:180px;width:328px;height:48px;background:#fff;border-radius:6px;color:#777;font-size:13px;padding:15px 22px}
.sub-btn{position:absolute;left:116px;top:242px;width:118px;height:42px;background:var(--green);color:#fff;font-weight:700;font-size:15px;display:flex;align-items:center;justify-content:center;border-radius:3px}
.fcol{position:absolute;top:70px}
.fcol h5{font-size:21px;font-weight:500;margin-bottom:16px}
.fcol a{display:block;color:#fff;text-decoration:none;font-size:13px;line-height:30px;padding-left:4px}
.contact-row{display:flex;align-items:center;gap:16px;font-size:13px;margin-bottom:26px}
.contact-row i{width:24px;height:24px;border-radius:50%;background:#fff;display:flex;align-items:center;justify-content:center}
.contact-row i svg{width:13px;height:13px;fill:#121212}
.social{position:absolute;left:884px;top:300px;display:flex;gap:7px}
.social i{width:28px;height:28px;border-radius:50%;background:#fff}
.social i:first-child{background:var(--blue)}
.copy{position:absolute;left:106px;top:334px;width:982px;border-top:1px solid #555;text-align:center;font-size:12px;padding-top:6px}
</style>
</head>
<body>

<header class="site-header">
  <div class="brand"><div class="brand-name">VORMINTA</div><div class="brand-tag">PLASTIC TO DIESEL ENERGY</div></div>
  <div class="topbar">
    <span><svg viewBox="0 0 24 24"><path d="M6.6 10.8a15 15 0 006.6 6.6l2.2-2.2c.3-.3.7-.4 1-.2 1.1.4 2.3.6 3.6.6.6 0 1 .4 1 1V20c0 .6-.4 1-1 1A17 17 0 013 4c0-.6.4-1 1-1h3.5c.6 0 1 .4 1 1 0 1.3.2 2.5.6 3.6.1.3 0 .7-.2 1z"/></svg>+1 888 888 8888</span>
    <span><svg viewBox="0 0 24 24"><path d="M2 5h20v14H2z M2 5l10 8 10-8" /></svg>info@vorminta.com</span>
    <span><svg viewBox="0 0 24 24"><path d="M12 2a7 7 0 00-7 7c0 5 7 13 7 13s7-8 7-13a7 7 0 00-7-7zm0 9.5a2.5 2.5 0 110-5 2.5 2.5 0 010 5z"/></svg>Lorem Ipsum,USA - 437916</span>
  </div>
  <nav class="nav">
    <a class="active" href="#">Home</a><a href="#">Technology</a><a href="#">Environmental Impact</a><a href="#">Industries</a><a href="#">About Us</a><a href="#">Contact</a>
  </nav>
</header>

<section class="hero">
  <h1>Turning Plastic Waste Into <em>Clean Diesel Energy</em></h1>
  <p>Vorminta converts discarded plastic into usable diesel fuel — reducing landfill waste while creating reliable energy for commercial diesel buyers.</p>
  <div class="actions"><a class="btn btn-green" href="#">Learn How It Works</a><a class="btn btn-white" href="#">Contact Our Team</a></div>
  <div class="hero-art" role="img" aria-label="Recycling loop made of plastic bottles and cans around a green bottle"></div>
</section>

<h2 class="sec-title" style="top:778px">Industries <b>We Serve</b></h2>
<p class="sub">Vorminta fuel solutions are designed for industries that rely on diesel for daily operations.</p>

<div class="arrow prev" style="left:41px;top:1063px"><svg viewBox="0 0 14 14"><path d="M9 2L4 7l5 5"/></svg></div>
<div class="card" style="left:110px">
  <div class="ph" role="img" aria-label="Red semi truck on a highway" style="background:linear-gradient(180deg,#9fb98a,#6d7a70 55%,#5a5d60)"></div>
  <h3>Trucking &amp; Logistics</h3>
</div>
<div class="card feature" style="left:445px">
  <div class="ph" role="img" aria-label="Young green plant sprouting from soil" style="background:radial-gradient(circle at 50% 60%,#6fcf5a,#1f5a2a 70%,#0f2a18)"></div>
  <div class="badge"><svg width="24" height="24" viewBox="0 0 24 24" fill="none" stroke="#7cc242" stroke-width="2"><path d="M12 21V11M12 11c0-4-3-6-7-6 0 4 3 6 7 6zM12 13c0-4 3-6 7-6 0 4-3 6-7 6z"/></svg></div>
  <h3>Agricultural Operations</h3>
  <p>Modern farming depends on diesel-powered machinery including tractors, harvesters, irrigation systems, and transport vehicles.</p>
</div>
<div class="card" style="left:779px">
  <div class="ph" role="img" aria-label="Construction workers in safety vests at a building site" style="background:linear-gradient(180deg,#b89a78,#8a7a66 55%,#6f6a60)"></div>
  <h3>Construction Companie</h3>
</div>
<div class="arrow next" style="left:1127px;top:1063px"><svg viewBox="0 0 14 14"><path d="M5 2l5 5-5 5"/></svg></div>

<section class="how">
  <h2 class="sec-title">How <b>It Works</b></h2>
  <div class="step" style="left:110px">
    <div class="ic blue"><svg viewBox="0 0 40 40" fill="#fff"><rect x="8" y="14" width="8" height="18"/><rect x="18" y="10" width="6" height="22"/><rect x="26" y="18" width="8" height="14"/></svg></div>
    <div class="ribbon w">STEP 1</div>
    <h4>Plastic Collection</h4>
    <p>Waste plastics are collected from recycling streams, industrial waste sources, and municipal waste facilities.</p>
  </div>
  <div class="step" style="left:360px">
    <div class="ic white"><svg viewBox="0 0 40 40" fill="none" stroke="#1a6fb8" stroke-width="3"><circle cx="20" cy="20" r="12"/><circle cx="20" cy="20" r="5"/></svg></div>
    <div class="ribbon b">STEP 2</div>
    <h4>Conversion Process</h4>
    <p>Using advanced thermal conversion technology, plastics are broken down into hydrocarbon compounds.</p>
  </div>
  <div class="step" style="left:610px">
    <div class="ic blue"><svg viewBox="0 0 40 40" fill="#fff"><rect x="8" y="20" width="24" height="12"/><rect x="12" y="8" width="6" height="12"/><rect x="22" y="12" width="6" height="8"/></svg></div>
    <div class="ribbon w2">STEP 3</div>
    <h4>Fuel Production</h4>
    <p>The hydrocarbons are refined into diesel-grade fuel suitable for commercial use.</p>
  </div>
  <div class="step" style="left:860px">
    <div class="ic white"><svg viewBox="0 0 40 40" fill="#1a6fb8"><path d="M23 4L10 22h9l-3 14 14-19h-9z"/></svg></div>
    <div class="ribbon b">STEP 4</div>
    <h4>Energy Distribution</h4>
    <p>The fuel is supplied to commercial diesel buyers including logistics, transportation, agriculture, and industrial sectors.</p>
  </div>
</section>

<section class="about">
  <div class="about-img" role="img" aria-label="Workers in hard hats sorting plastic waste at a recycling plant"></div>
  <h2>About <b>Us</b></h2>
  <p style="top:2012px">Vorminta is an innovative energy company focused on transforming plastic waste into valuable diesel fuel. Our mission is to address two global challenges at once — reducing plastic pollution and creating sustainable energy solutions for industries that rely on diesel every day.</p>
  <p style="top:2141px">Every year, millions of tons of plastic waste end up in landfills and oceans, causing long-term environmental damage. At Vorminta, we believe that waste should not be wasted.</p>
  <a class="btn btn-green abs" style="left:643px;top:2251px;padding:11px 19px" href="#">Read More</a>
</section>

<section class="why">
  <h2 class="sec-title">Why <b>Choose &nbsp;Us</b></h2>
  <div class="emblem" role="img" aria-label="Recycling arrows surrounding a flame"></div>
  <div class="why-item l" style="left:130px;top:172px;width:330px">
    <h4>Compelling Value Proposition</h4>
    <p>A proprietary, continuous-flow technology that converts plastic waste into high-grade diesel, addressing two global challenges simultaneously:.</p>
  </div>
  <div class="why-ic" style="left:468px;top:170px"><svg viewBox="0 0 30 30" fill="none" stroke="#1a6fb8" stroke-width="2.5"><path d="M8 8h14l-7 10z M5 22c4 0 6 2 10 2s6-2 10-2"/></svg></div>
  <div class="why-ic" style="left:664px;top:170px"><svg viewBox="0 0 30 30" fill="none" stroke="#1a6fb8" stroke-width="2.5"><rect x="6" y="10" width="18" height="10"/><circle cx="15" cy="15" r="3"/></svg></div>
  <div class="why-item" style="left:744px;top:182px;width:330px">
    <h4>Attractive Financial Returns</h4>
    <p>With annual gross revenue potential of US$ 2.5-4.5 million per unit, EBITDA margins of 30–45%, IRR of 28.5% and an indicative payback period of 5 years,</p>
  </div>
  <div class="why-item l" style="left:60px;top:354px;width:330px">
    <h4>Proven, Scalable Unit Economics</h4>
    <p>Each US$4 million modular unit processes 1 ton of plastic per hour, producing approximately 16,800 liters of diesel per day through 24/7 continuous</p>
  </div>
  <div class="why-ic" style="left:402px;top:348px"><svg viewBox="0 0 30 30" fill="#1a6fb8"><rect x="6" y="16" width="4" height="8"/><rect x="12" y="11" width="4" height="13"/><rect x="18" y="7" width="4" height="17"/></svg></div>
  <div class="why-ic" style="left:724px;top:348px"><svg viewBox="0 0 30 30" fill="#1a6fb8"><path d="M12 6h6v9h5l-8 9-8-9h5z"/></svg></div>
  <div class="why-item" style="left:811px;top:354px;width:300px">
    <h4>Low Execution Risk</h4>
    <p>Backed by secured feedstock supply chains and confirmed diesel offtake partners, ensuring operational continuity, revenue visibility,</p>
  </div>
</section>

<h2 class="sec-title" style="top:3036px">Meeth <b style="font-weight:400">The Team</b></h2>
<div class="arrow prev" style="left:40px;top:3265px"><svg viewBox="0 0 14 14"><path d="M9 2L4 7l5 5"/></svg></div>
<div class="member" style="left:106px"><div class="ph" role="img" aria-label="Portrait of team member Maren" style="background:linear-gradient(160deg,#d9d3c8,#8a7060 60%,#2f4a3c)"></div><span>Maren</span></div>
<div class="member" style="left:355px"><div class="ph" role="img" aria-label="Portrait of team member Tobin" style="background:linear-gradient(160deg,#e8d2b8,#c9a88a 60%,#2a3040)"></div><span>Tobin</span></div>
<div class="member" style="left:603px"><div class="ph" role="img" aria-label="Portrait of team member Lisel" style="background:linear-gradient(160deg,#b8bcc0,#d7b98f 55%,#6a6f4f)"></div><span>Lisel</span></div>
<div class="member" style="left:852px"><div class="ph" role="img" aria-label="Portrait of team member Corvan" style="background:linear-gradient(160deg,#8a8d90,#6e7073 55%,#c7b59a)"></div><span>Corvan</span></div>
<div class="arrow next" style="left:1126px;top:3265px"><svg viewBox="0 0 14 14"><path d="M5 2l5 5-5 5"/></svg></div>

<footer class="footer">
  <div class="brand"><div class="brand-name">VORMINTA</div><div class="brand-tag">PLASTIC TO DIESEL ENERGY</div></div>
  <div class="sub-form">Enter Email Address</div>
  <div class="sub-btn">Subscribe</div>
  <div class="fcol" style="left:503px;top:74px"><h5>Quick Links</h5><a>Home</a><a>Technology</a><a>Environmental Impact</a><a>Industries</a><a>About Us</a><a>Contact</a></div>
  <div class="fcol" style="left:683px"><h5>Other Links</h5><a>Privacy Policy</a><a>Terms &amp; Conditions</a><a>FAQ;s</a><a>Disclaimer</a><a>Support</a><a>Help</a></div>
  <div class="fcol" style="left:888px"><h5>Contact Info</h5>
    <div class="contact-row"><i><svg viewBox="0 0 24 24"><path d="M12 2a7 7 0 00-7 7c0 5 7 13 7 13s7-8 7-13a7 7 0 00-7-7z"/></svg></i>Lorem Ipsum,USA -437916</div>
    <div class="contact-row"><i><svg viewBox="0 0 24 24"><path d="M6.6 10.8a15 15 0 006.6 6.6l2.2-2.2c.3-.3.7-.4 1-.2 1.1.4 2.3.6 3.6.6.6 0 1 .4 1 1V20c0 .6-.4 1-1 1A17 17 0 013 4c0-.6.4-1 1-1h3.5c.6 0 1 .4 1 1 0 1.3.2 2.5.6 3.6z"/></svg></i>+1 888 888 8888</div>
    <div class="contact-row"><i><svg viewBox="0 0 24 24"><path d="M3 6h18v12H3z"/></svg></i>info@vorminta.com</div>
  </div>
  <div class="social"><i></i><i></i><i></i><i></i><i></i></div>
  <div class="copy">© 2026 &nbsp;Vorminta.All rights reserved</div>
</footer>

</body>
</html>
```